Fernbrook Plots - Online-only garden installation company

Online-only garden installation company. Our demographic is middle aged / suburban women, and we anticipate Facebook driving traffic to this website, as well as referrals from garden centers. The website must be very simple in design and function.

All orders will be placed through the website, including size of garden (3 options), location in yard, payment, and scheduling of installation date.

The website should employ a 3 step process:

Step 1: Select garden size. Either an 4' X 4', 8' X 4', or 12' X 4'.

Step 2: Select a location. We would like to use google maps to look up a US address, then "drag and drop" one of the garden sizes from step 1 to the location the customer would like us to install the garden at their home.

Step 3: Pick an installation date and pay. Using an online calendar the customer will pick a date, and then pay for the installation via credit card.

The website will be linked to an email account, FernbrookPlots@mailzy.com to inform us of orders placed.

Target Market(s)

Our demographic is middle aged / suburban women, and we anticipate Facebook driving traffic to this website, as well as referrals from garden centers.

Industry/Entity Type

Coding

Number of Pages Required

Requirements
Must have
• Scheduling and payment options.

```html
<!DOCTYPE html>
<html lang="en">
<head>
<meta charset="utf-8">
<title>Fernbrook Plots – Garden Installation</title>
<link href="https://fonts.googleapis.com/css2?family=Alfa+Slab+One&family=Glegoo&family=Ubuntu:wght@400;500&display=swap" rel="stylesheet">
<style>
:root{
  --white:#ffffff;
  --line:#dcdcdc;
  --ink:#444444;
  --muted:#555555;
  --green:#3a803d;
  --orange:#e15a2b;
  --orange-dark:#b8421c;
  --footer:#f1f1f1;
  --field-btn:#dedede;
  --social:#8c8c8c;
}
*{box-sizing:border-box;margin:0;padding:0}
html,body{width:1200px;height:1092px;overflow:hidden;background:var(--white)}
body{position:relative;font-family:"Ubuntu",sans-serif;color:var(--ink)}
.site-header{position:absolute;left:0;top:0;width:1200px;height:75px;background:var(--white);z-index:2}
.brand-box{position:absolute;left:74px;top:0;width:152px;height:144px;background:var(--white);display:flex;flex-direction:column;align-items:center;justify-content:center;gap:8px;z-index:3}
.brand-mark{width:22px;height:22px;border-radius:50%;background:var(--orange)}
.brand-name{font-family:"Glegoo",serif;font-size:15px;color:var(--ink);text-align:center;line-height:1.2}
.header-nav{position:absolute;right:0;top:0;height:75px;display:flex}
.nav-item{height:75px;border-left:1px solid var(--line);display:flex;align-items:center;justify-content:center;width:80px}
.nav-item.account{width:248px;justify-content:flex-start;padding-left:30px;gap:10px;font-size:13.5px;color:var(--muted)}
.hero{position:absolute;left:0;top:75px;width:1200px;height:534px;
  background:linear-gradient(115deg,#7fa62a 0%,#93b737 35%,#a2b04a 55%,#7d6a4f 75%,#5f5243 100%)}
.hero-frame{position:absolute;left:346px;top:190px;width:508px;height:156px;border:3px solid var(--white);text-align:center}
.hero-title{font-family:"Alfa Slab One",serif;font-size:37px;color:var(--white);letter-spacing:1px;margin-top:36px;line-height:1}
.ribbon{position:relative;display:inline-block;margin-top:4px;height:28px;padding:0 14px;background:var(--orange);color:var(--white);font-family:"Glegoo",serif;font-size:18px;line-height:28px}
.ribbon::before,.ribbon::after{content:"";position:absolute;top:6px;width:40px;height:20px;background:var(--orange-dark);z-index:-1}
.ribbon::before{left:-32px}
.ribbon::after{right:-32px}
.order-band{position:absolute;left:0;top:609px;width:1200px;height:204px;background:var(--green)}
.order-title{position:absolute;left:0;top:38px;width:1200px;text-align:center;font-family:"Glegoo",serif;font-size:30px;color:var(--white)}
.field{position:absolute;top:112px;width:243px;height:46px;background:var(--white);border-radius:3px;display:flex;align-items:center;justify-content:space-between;padding:0 3px 0 13px;font-size:13.5px;color:#666}
.field-btn{width:40px;height:40px;background:var(--field-btn);border-radius:2px;display:flex;align-items:center;justify-content:center}
.search-btn{position:absolute;left:915px;top:112px;width:127px;height:46px;background:var(--orange);border-radius:2px;display:flex;align-items:center;justify-content:center;gap:10px;color:var(--white);font-size:16px;font-weight:500}
.site-footer{position:absolute;left:0;top:813px;width:1200px;height:279px;background:var(--footer)}
.footer-heading{font-family:"Glegoo",serif;font-size:16.5px;color:var(--ink);position:absolute;top:45px}
.about-text{position:absolute;left:74px;top:84px;width:340px;font-size:13.5px;line-height:22px;color:var(--muted)}
.support-list{position:absolute;left:513px;top:84px;list-style:none;font-size:13.5px;line-height:22px;color:var(--muted)}
.social{position:absolute;left:728px;top:83px;display:flex;gap:5px}
.social span{width:37px;height:37px;background:var(--social)}
.footer-brand{position:absolute;left:978px;top:60px;width:144px;display:flex;flex-direction:column;align-items:center;gap:10px}
.copyright{position:absolute;left:73px;top:233px;font-size:13.5px;color:var(--muted)}
.legal{position:absolute;right:75px;top:233px;font-size:13.5px;color:var(--muted)}
</style>
</head>
<body>
<header class="site-header">
  <div class="brand-box">
    <span class="brand-mark"></span>
    <span class="brand-name">FERNBROOK PLOTS</span>
  </div>
  <nav class="header-nav">
    <div class="nav-item">
      <svg width="26" height="26" viewBox="0 0 26 26" fill="none" stroke="#777" stroke-width="1.6"><circle cx="11" cy="11" r="9"/><line x1="17.5" y1="17.5" x2="24" y2="24"/></svg>
    </div>
    <div class="nav-item">
      <svg width="26" height="24" viewBox="0 0 26 24" fill="none" stroke="#777" stroke-width="1.5"><path d="M1 3h4l3 13h14l2-10H7"/><line x1="10" y1="9" x2="21" y2="9"/><line x1="10" y1="12" x2="20" y2="12"/><circle cx="10" cy="20" r="1.6"/><circle cx="20" cy="20" r="1.6"/></svg>
    </div>
    <div class="nav-item account">
      <svg width="22" height="26" viewBox="0 0 22 26" fill="none" stroke="#777" stroke-width="1.5"><circle cx="11" cy="8" r="6"/><path d="M1 25v-3a6 6 0 0 1 6-6h8a6 6 0 0 1 6 6v3z"/></svg>
      <span>LOGIN / SIGN UP</span>
    </div>
  </nav>
</header>

<section class="hero" role="img" aria-label="Photo of fresh lawn with rolls of turf laid beside a soil bed and curved stone edging">
  <div class="hero-frame">
    <h1 class="hero-title">FERNBROOK PLOTS</h1>
    <div class="ribbon">Only Garden Installation Company</div>
  </div>
</section>

<section class="order-band">
  <h2 class="order-title">Order Now Garden Installation Today</h2>
  <div class="field" style="left:159px">Select garden size
    <span class="field-btn"><svg width="10" height="8" viewBox="0 0 10 8"><path d="M0 0h10L5 8z" fill="#666"/></svg></span>
  </div>
  <div class="field" style="left:411px">Select a location
    <span class="field-btn"><svg width="22" height="22" viewBox="0 0 22 22" fill="none" stroke="#777" stroke-width="1.6"><circle cx="11" cy="11" r="7"/><circle cx="11" cy="11" r="3" fill="#777"/><path d="M11 1v3M11 18v3M1 11h3M18 11h3"/></svg></span>
  </div>
  <div class="field" style="left:663px">Pick an installation date
    <span class="field-btn"><svg width="22" height="22" viewBox="0 0 22 22" fill="none" stroke="#777" stroke-width="1.5"><rect x="2" y="4" width="18" height="16"/><line x1="2" y1="8" x2="20" y2="8"/><path d="M6 2v4M16 2v4"/><g fill="#777" stroke="none"><rect x="5" y="10" width="2" height="2"/><rect x="9" y="10" width="2" height="2"/><rect x="13" y="10" width="2" height="2"/><rect x="5" y="14" width="2" height="2"/><rect x="9" y="14" width="2" height="2"/><rect x="13" y="14" width="2" height="2"/></g></svg></span>
  </div>
  <div class="search-btn">
    <svg width="22" height="22" viewBox="0 0 22 22" fill="none" stroke="#fff" stroke-width="1.8"><circle cx="9" cy="9" r="7.5"/><line x1="14.5" y1="14.5" x2="21" y2="21"/></svg>
    SEARCH
  </div>
</section>

<footer class="site-footer">
  <h3 class="footer-heading" style="left:73px">About Fernbrook Plots</h3>
  <p class="about-text">Lorem ipsum dolor sit amet, consectetur adipisicing elit, sed do eiusmod tempor incididunt ut labore et dolore magna aliqua. Ut enim ad minim veniam, quis nostrud exercitation ullamco laboris nisi ut aliquip ex fugiat nulla pariatur.</p>
  <h3 class="footer-heading" style="left:512px">Customer Support</h3>
  <ul class="support-list">
    <li>My Account</li><li>Shopping Cart</li><li>FAQ</li><li>Help!</li><li>Newsletter</li>
  </ul>
  <h3 class="footer-heading" style="left:728px">We’re Social Media</h3>
  <div class="social"><span></span><span></span><span></span><span></span></div>
  <div class="footer-brand">
    <span class="brand-mark"></span>
    <span class="brand-name">FERNBROOK PLOTS</span>
  </div>
  <p class="copyright">Copyright © 2017 Fernbrook Plots. All Rights Reserved</p>
  <p class="legal">Terms of Use | Privacy Policy | Sitemap</p>
</footer>
</body>
</html>
```